photowall advertisement

We require a wall featuring our company logo. We would like to avoid the color green, and gold is highly preferred. The design should be similar to the one in the attached photo. The wall will be used for photos and promotional purposes during congresses. Files must be prepared for printing.
dimension of wall: 470x223 cm

Industry/Entity Type

lifestyle

Colors
0054AA
0677BA
7BADD7
CADEEF
E8F1F8
6B429C
8869AF
B7A5CE
E3DAEB
F3F0F8

Requirements
Must have
• gold color, white, and other compare with gold color
Nice to have
• some pictograms, maps of Europe

```html
<!DOCTYPE html>
<html lang="en">
<head>
<meta charset="utf-8">
<title>Halvern Technology – Photowall</title>
<link rel="stylesheet" href="https://fonts.googleapis.com/css2?family=Exo+2:wght@500&display=swap">
<style>
  :root {
    --backdrop: #7b633d;
    --gold: #cba972;
    --gold-deep: #b8914f;
    --white: #ffffff;
    --shadow: rgba(0, 0, 0, 0.35);
  }
  * { margin: 0; padding: 0; box-sizing: border-box; }
  html, body {
    width: 936px; height: 1200px; overflow: hidden;
    background: var(--backdrop);
    font-family: "Exo 2", sans-serif;
    font-weight: 500;
  }
  .photowall {
    position: absolute;
    left: 28px; top: 391px;
    width: 880px; height: 418px;
    overflow: hidden;
    box-shadow: 0 12px 30px var(--shadow);
  }
  .photowall__field {
    position: absolute; inset: 0;
    background: var(--gold);
  }
  .tile-row {
    position: absolute; left: 0;
    display: flex; height: 57px;
  }
  .tile-row--1 { top: 0; margin-left: -10px; }
  .tile-row--2 { top: 57px; margin-left: -10px; }
  .tile-row--3 { top: 304px; margin-left: -22px; }
  .tile-row--4 { top: 361px; margin-left: -22px; }
  .tile {
    flex: 0 0 79px; height: 57px;
    display: flex; align-items: center; justify-content: center;
    text-transform: uppercase;
  }
  .tile--light { background: var(--white); color: var(--gold); font-size: 12px; letter-spacing: 1px; }
  .tile--gold { background: var(--gold); color: var(--white); font-size: 28px; letter-spacing: 1px; }
  .brand-lockup {
    position: absolute; left: 0; right: 0; top: 182px;
    text-align: center;
    color: var(--white);
    font-size: 34px;
    letter-spacing: 6px;
    text-transform: uppercase;
  }
</style>
</head>
<body>
  <main class="photowall">
    <div class="photowall__field" role="img" aria-label="Gold field with a fine grid of lines and dots"></div>

    <div class="tile-row tile-row--1">
      <div class="tile tile--light">Halvern</div><div class="tile tile--gold">HV</div>
      <div class="tile tile--light">Halvern</div><div class="tile tile--gold">HV</div>
      <div class="tile tile--light">Halvern</div><div class="tile tile--gold">HV</div>
      <div class="tile tile--light">Halvern</div><div class="tile tile--gold">HV</div>
      <div class="tile tile--light">Halvern</div><div class="tile tile--gold">HV</div>
      <div class="tile tile--light">Halvern</div><div class="tile tile--gold">HV</div>
    </div>
    <div class="tile-row tile-row--2">
      <div class="tile tile--gold">HV</div><div class="tile tile--light">Halvern</div>
      <div class="tile tile--gold">HV</div><div class="tile tile--light">Halvern</div>
      <div class="tile tile--gold">HV</div><div class="tile tile--light">Halvern</div>
      <div class="tile tile--gold">HV</div><div class="tile tile--light">Halvern</div>
      <div class="tile tile--gold">HV</div><div class="tile tile--light">Halvern</div>
      <div class="tile tile--gold">HV</div><div class="tile tile--light">Halvern</div>
    </div>

    <div class="brand-lockup">Halvern Technology</div>

    <div class="tile-row tile-row--3">
      <div class="tile tile--light">Halvern</div><div class="tile tile--gold">HV</div>
      <div class="tile tile--light">Halvern</div><div class="tile tile--gold">HV</div>
      <div class="tile tile--light">Halvern</div><div class="tile tile--gold">HV</div>
      <div class="tile tile--light">Halvern</div><div class="tile tile--gold">HV</div>
      <div class="tile tile--light">Halvern</div><div class="tile tile--gold">HV</div>
      <div class="tile tile--light">Halvern</div><div class="tile tile--gold">HV</div>
    </div>
    <div class="tile-row tile-row--4">
      <div class="tile tile--gold">HV</div><div class="tile tile--light">Halvern</div>
      <div class="tile tile--gold">HV</div><div class="tile tile--light">Halvern</div>
      <div class="tile tile--gold">HV</div><div class="tile tile--light">Halvern</div>
      <div class="tile tile--gold">HV</div><div class="tile tile--light">Halvern</div>
      <div class="tile tile--gold">HV</div><div class="tile tile--light">Halvern</div>
      <div class="tile tile--gold">HV</div><div class="tile tile--light">Halvern</div>
    </div>
  </main>
</body>
</html>
```